Microlight Aircraft Website Project

Need a website designed, or at least a template made, that my web programmer can work with here. We are a new manufacturer of microlight aircraft & powered hang gliders. Our company name is Brisk Fern. We manufacture portable utility aircraft in the Light Sport category (formerly known as Ultralights or Microlights). Our particular design is a 2-seat powered hang glider and caters to those who want to go explore the backcountry. We are not necessarily aviation nuts, but more into the development of a flying utility vehicle for extreme exploration and expeditions. We have been importing these aircraft from 3 countries for 15 years and have supplied over 200 expedition-quality aircraft world-wide. We are now manufacturing here in the US.

Industry/Entity Type

Manufacturer

Coding

Coded - Design and coding required

```html
<!DOCTYPE html>
<html lang="en">
<head>
<meta charset="utf-8">
<title>Brisk Fern — Contact</title>
<link href="https://fonts.googleapis.com/css2?family=Raleway:wght@200;300;400;600;700;800&display=swap" rel="stylesheet">
<style>
:root{
  --ink:#3a3956;
  --ink-deep:#33324d;
  --muted:#a3a3a8;
  --field:#f1f1f1;
  --white:#ffffff;
  --rule:#b9b9c4;
  --sky-top:#c9ccd0;
  --sky-mid:#8fa7b8;
  --glacier:#1f8fae;
  --map-a:#e6e6e6;
  --map-b:#d4d4d4;
  --banner-top:#8ea6c2;
  --banner-bottom:#314a6e;
  --dock:#2b2b2b;
  --social:#4a4a66;
}
*{margin:0;padding:0;box-sizing:border-box}
html,body{width:1200px;height:2400px;overflow:hidden;background:var(--white)}
body{position:relative;font-family:'Raleway',sans-serif;color:var(--ink)}
.abs{position:absolute}

/* Hero */
.hero{left:0;top:0;width:1200px;height:416px;
  background:linear-gradient(180deg,var(--sky-top) 0%,#b7c2cb 30%,var(--sky-mid) 55%,#3f9cb8 78%,var(--glacier) 100%)}
.brand{left:115px;top:38px;display:flex;align-items:center;gap:10px;color:var(--white);
  font-weight:700;font-size:20px;letter-spacing:2px}
.brand-dot{width:14px;height:14px;border-radius:50%;background:var(--white)}
.nav{top:49px;left:0;width:1200px;height:14px}
.nav a{position:absolute;color:var(--white);text-decoration:none;font-size:11px;font-weight:700;letter-spacing:.3px}
.dock{left:1162px;width:38px;height:32px;background:var(--dock);display:flex;align-items:center;justify-content:center}
.hero-kicker{left:0;width:1250px;top:200px;text-align:center;color:var(--white);font-size:16px;font-weight:300;letter-spacing:.5px}
.hero-title{left:0;width:1250px;top:228px;text-align:center;color:var(--white);font-size:50px;letter-spacing:-.5px}
.hero-title b,.banner-title b{font-weight:700}
.hero-title span,.banner-title span{font-weight:200}

/* Contact */
.contact-heading{left:75px;top:504px;font-size:52px;font-weight:700;color:var(--ink-deep);letter-spacing:.5px}
.contact-rule{left:419px;top:536px;width:103px;height:2px;background:var(--rule)}
.intro{left:77px;top:602px;width:510px;font-size:13.5px;line-height:20px;font-weight:300;color:var(--muted)}
.intro p+p{margin-top:20px}
.info-col{top:764px}
.info-col h3{font-size:13px;font-weight:700;color:var(--ink-deep);margin-bottom:12px}
.info-col p{font-size:13px;line-height:21px;font-weight:300;color:var(--muted)}
.field{left:658px;width:457px;background:var(--field);padding:18px 20px;font-size:10.5px;font-weight:700;letter-spacing:.8px;color:#6c6c78}
.send{left:659px;top:918px;width:189px;height:37px;background:var(--ink);color:var(--white);
  font-size:13px;font-weight:700;display:flex;align-items:center;padding-left:23px}
.send svg{position:absolute;right:14px;top:13px}

/* Map */
.map{left:0;top:1077px;width:1200px;height:507px;
  background:linear-gradient(180deg,var(--map-a) 0%,#e9e9e9 70%,var(--map-b) 72%,var(--map-b) 100%)}

/* Banner */
.banner{left:0;top:1664px;width:1200px;height:272px;
  background:linear-gradient(180deg,var(--banner-top) 0%,#7088a8 40%,#44607f 70%,var(--banner-bottom) 100%)}
.banner-kicker{left:0;width:1200px;top:1788px;text-align:center;color:var(--white);font-size:19px;font-weight:300}
.banner-title{left:0;width:1200px;top:1802px;text-align:center;color:var(--white);font-size:48px}

/* Footer */
.foot-brand{left:0;width:1200px;top:2020px;display:flex;justify-content:center;align-items:center;gap:10px;
  font-size:20px;font-weight:700;letter-spacing:2px;color:#1c1c1c}
.foot-brand i{width:14px;height:14px;border-radius:50%;background:#1c1c1c}
.social{left:494px;top:2106px;display:flex;gap:7px}
.social i{width:29px;height:29px;border-radius:50%;background:var(--social)}
.foot-heading{left:0;width:1200px;top:2173px;text-align:center;font-size:16px;font-weight:700;color:#111}
.foot-line{left:0;width:1200px;text-align:center;font-size:12px;font-weight:400;color:var(--muted)}
.foot-links{left:0;width:1200px;top:2282px;text-align:center;font-size:12px;color:var(--muted);letter-spacing:.3px}
.copyright{left:0;width:1200px;top:2315px;text-align:center;font-size:11px;color:var(--muted)}
</style>
</head>
<body>

<header>
  <div class="abs hero" role="img" aria-label="Photo of snow-capped mountain range under a cloudy sky with a hang glider in flight"></div>
  <div class="abs brand"><span class="brand-dot"></span>BRISK FERN</div>
  <nav class="abs nav">
    <a style="left:567px">HOME</a>
    <a style="left:645px">ABOUT US</a>
    <a style="left:748px">GLIDERS</a>
    <a style="left:842px">ACCESSORIES</a>
    <a style="left:965px">STORE</a>
    <a style="left:1047px">CONTACT</a>
  </nav>
  <div class="abs dock" style="top:112px" aria-label="Cart">
    <svg width="16" height="14" viewBox="0 0 16 14"><path d="M0 1h3l2 8h8l2-6H4" fill="none" stroke="#fff" stroke-width="1.6"/><circle cx="6" cy="12" r="1.3" fill="#fff"/><circle cx="12" cy="12" r="1.3" fill="#fff"/></svg>
  </div>
  <div class="abs dock" style="top:154px" aria-label="Wishlist">
    <svg width="14" height="13" viewBox="0 0 14 13"><path d="M7 12.5 1.2 6.8A3.4 3.4 0 0 1 7 2.2a3.4 3.4 0 0 1 5.8 4.6z" fill="#fff"/></svg>
  </div>
  <div class="abs hero-kicker">WRITE TO US, CHANCES ARE...</div>
  <h1 class="abs hero-title"><b>WE MIGHT</b> <span>WRITE YOU</span> <b>BACK</b></h1>
</header>

<main>
  <h2 class="abs contact-heading">CONTACT US</h2>
  <div class="abs contact-rule"></div>
  <div class="abs intro">
    <p>We are a new manufacturer of microlight aircraft &amp; powered hang gliders. Our company name is Brisk Fern. We manufacture portable utility aircraft in the Light Sport category (formerly known as Ultralights or Microlights).</p>
    <p>&nbsp;Our particular design is a 2-seat powered hang glider and caters to those who want to go explore the backcountry.</p>
  </div>
  <div class="abs info-col" style="left:77px">
    <h3>ADDRESS</h3>
    <p>27 Alder Quay<br>Lowmarsh<br>PO Box 4410</p>
  </div>
  <div class="abs info-col" style="left:253px">
    <h3>WEB</h3>
    <p>E: hello@briskfern-air.com<br>P: +325 6170 4382</p>
  </div>

  <form>
    <div class="abs field" style="top:603px;height:51px">YOUR NAME</div>
    <div class="abs field" style="top:678px;height:50px">EMAIL ADDRESS</div>
    <div class="abs field" style="top:752px;height:128px">MESSAGE</div>
    <div class="abs send">SEND MESSAGE
      <svg width="8" height="12" viewBox="0 0 8 12"><path d="M1.5 1l5 5-5 5" fill="none" stroke="#fff" stroke-width="1.8"/></svg>
    </div>
  </form>

  <div class="abs map" role="img" aria-label="Greyscale street map of the coastal neighbourhood around the office, with a location pin"></div>

  <section>
    <div class="abs banner" role="img" aria-label="Photo of a green hang glider soaring over blue mountain ridges"></div>
    <div class="abs banner-kicker">LIVE YOUR DREAM</div>
    <h2 class="abs banner-title"><b>COME</b> <span>FLY WITH</span> <b>US!</b></h2>
  </section>
</main>

<footer>
  <div class="abs foot-brand"><i></i>BRISK FERN</div>
  <div class="abs social"><i></i><i></i><i></i><i></i><i></i><i></i></div>
  <div class="abs foot-heading">CONTACT US</div>
  <div class="abs foot-line" style="top:2198px">812 N. CEDAR HOLLOW, PINECREST, CA 90417, USA</div>
  <div class="abs foot-line" style="top:2220px">TELEPHONE: 555-204-7731 &nbsp;&nbsp;&nbsp;|&nbsp;&nbsp;&nbsp; FAX: 555-204-7790</div>
  <div class="abs foot-links">PRIVACY POLICY &nbsp;/&nbsp; TERMS &amp; CONDITIONS &nbsp;/&nbsp; FAQS</div>
  <div class="abs copyright">© COPYRIGHT 2016 BRISK FERN. ALL RIGHTS RESERVED</div>
</footer>

</body>
</html>
```